Luxurious Rustic Cottage Accommodation brochure design

I would like a trifold brochure design to continue the theme I already have established on my website www.atbellcroft.com.au The basic theme uses the logo from the website, it is called "At Bellcroft" B & B Private Cottages and has black background with use of gold for borders and highlights. The accommodation is in the hinterland region of the Sunshine Coast, Queensland, Australia. I have 4 separate private cottages which I would like to include information & pictures about each as per details on the website mentioned. Features to highlight include ocean views, log fires, spa baths, romance, nature. Accommodation is suitable for couples, family, small group or wedding party, special occasion getways. Package inclusions to be highlighted are breakfast hamper, complimentary chocolates & champagne, pamper products, optional inclusions are cheese platter, relaxation massage. I would like location to be included by way of a map, contact details (website, email & mobile phone) to also be included.
There are pictures on the website which I can provide high resolution for brochure printing as required. Some more images have been uploaded for optional use.
Accommodation

```html
<!DOCTYPE html>
<html lang="en">
<head>
<meta charset="utf-8">
<title>At Bellcroft – Trifold Brochure</title>
<link href="https://fonts.googleapis.com/css2?family=Cormorant+Garamond:ital,wght@0,400;0,600;1,500&family=Lato:wght@400;700&display=swap" rel="stylesheet">
<style>
  :root{
    --page:#ffffff;
    --charcoal-1:#1f1f1f;
    --charcoal-2:#3e3e3e;
    --ink:#2b2b2b;
    --white:#ffffff;
    --label:rgba(255,255,255,0.72);
    --muted:#d8d8d8;
    --web-bar:#5a5a5a;
    --serif:"Cormorant Garamond", Georgia, serif;
    --sans:"Lato", "Helvetica Neue", Arial, sans-serif;
  }
  *{box-sizing:border-box;margin:0;padding:0}
  html,body{width:1200px;height:767px;overflow:hidden;background:var(--page)}
  .canvas{position:relative;width:1200px;height:767px;overflow:hidden;background:var(--page)}

  .sheet{
    position:absolute;transform:rotate(90deg);transform-origin:center;
    background:radial-gradient(ellipse at 50% 40%,var(--charcoal-2),var(--charcoal-1) 85%);
    display:grid;grid-template-columns:1fr 1fr 1fr;column-gap:10px;padding:8px 6px;
    color:var(--white);font-family:var(--sans);
  }
  .sheet--inside{width:734px;height:572px;left:-63px;top:99px}
  .sheet--outside{width:740px;height:573px;left:526px;top:95px}

  .panel{display:flex;flex-direction:column;min-width:0}
  .panel-title{
    background:var(--white);color:var(--ink);font-family:var(--serif);
    font-size:21px;text-align:center;height:26px;line-height:26px;margin-bottom:6px;
  }

  .photo{border:0;flex:none}
  .photo--family{height:175px;background:linear-gradient(135deg,#6f8d5a,#c0302c 45%,#e6e0d8 70%,#5c6e47)}
  .about-text{font-size:12.4px;line-height:1.42;text-align:justify;text-align-last:left;padding:12px 12px 0}
  .about-sign{font-weight:700;text-align:right;text-align-last:right;padding-top:1px}
  .contact{text-align:center;font-size:12px;margin-top:20px;line-height:1.45}
  .contact strong{font-size:13px}

  .cabin-list{display:flex;flex-direction:column;gap:3px;flex:1;padding-bottom:12px}
  .cabin{position:relative;flex:1}
  .cabin--drovers{background:linear-gradient(120deg,#f4f2ee,#e9e4da 60%,#cdb58a)}
  .cabin--wattle{background:linear-gradient(120deg,#6b4a34,#a0784e 40%,#4e6a3a)}
  .cabin--kirra{background:linear-gradient(120deg,#dedbd3,#f3f1ec 50%,#8d8a79)}
  .cabin--lodge{background:linear-gradient(120deg,#6c8a4b,#c7c0ad 50%,#5b4a3a)}
  .cabin-label{
    position:absolute;left:80px;top:50%;transform:translateY(-50%);width:150px;
    background:var(--label);color:var(--ink);text-align:center;padding:6px 6px 8px;
  }
  .cabin-label h3{font-family:var(--serif);font-style:italic;font-weight:500;font-size:17px;line-height:1.1}
  .cabin-label p{font-family:var(--serif);font-size:9px;line-height:1.2}

  .rates{font-family:var(--serif);font-size:13px;padding:0 4px}
  .rate-head{background:var(--white);color:var(--ink);text-align:center;font-size:14px;font-weight:600;line-height:1.15;padding:5px 4px;margin:4px 0 10px}
  .rate-row{display:flex;justify-content:space-between;line-height:1.9}
  .rate-row.stack{line-height:1.2;margin-bottom:6px}
  .inclusions{font-family:var(--sans);text-align:center;font-size:12.5px;line-height:1.35;margin-top:28px}
  .inclusions h4{font-size:13px;font-weight:700;margin-top:8px}

  .map-title{
    background:var(--charcoal-1);color:var(--white);font-family:var(--sans);font-weight:700;
    font-size:13px;height:27px;line-height:27px;padding-left:6px;
  }
  .map{flex:1;position:relative;margin-bottom:12px;background:linear-gradient(160deg,#e7e5d9,#dfe3cf 40%,#e8e6da 70%,#d5dfc3)}
  .map svg{position:absolute;left:0;top:0}

  .middle{align-items:center;justify-content:flex-start;padding-top:260px;text-align:center}
  .brand-name{font-family:var(--serif);font-weight:400;font-size:42px;line-height:1;color:var(--white)}
  .brand-tag{font-family:var(--serif);font-size:11px;letter-spacing:.5px;margin:3px 0 8px}
  .address{font-family:var(--serif);font-size:13.5px;line-height:1.3}

  .front{padding-top:0}
  .hero{height:363px;position:relative;background:linear-gradient(180deg,#cfe0ef,#e8eff4 35%,#f1f1ee 55%,#cfd6d9 80%,#8b8b86)}
  .hero-brand{position:absolute;top:40px;left:0;right:0;text-align:center;color:var(--charcoal-1)}
  .hero-brand .brand-name{color:var(--charcoal-1);font-size:40px}
  .hero-brand .brand-tag{color:var(--charcoal-1)}
  .photo--hamper{height:65px;margin-top:10px;background:linear-gradient(120deg,#f5f4f0,#e6dfcf 60%,#c7a96d)}
  .photo--view{height:85px;margin-top:5px;background:linear-gradient(180deg,#8fb0cf,#6e8aa0 45%,#5d6b4e 75%,#a98a5c)}
  .web-bar{margin-top:6px;height:20px;background:var(--web-bar);color:var(--white);font-size:11.5px;line-height:20px;padding-left:8px;letter-spacing:.3px}
</style>
</head>
<body>
<div class="canvas">

  <!-- Inside sheet -->
  <section class="sheet sheet--inside">
    <article class="panel panel--about">
      <h2 class="panel-title">About Us</h2>
      <div class="photo photo--family" role="img" aria-label="Photo of the hosts and their daughters sitting on a red vintage car"></div>
      <p class="about-text">We are classic “treechangers” and together with our 3 daughters we moved to Queensland from Northern NSW in 2005 to enjoy the beautiful hinterland lifestyle and establish our B &amp; B. We love to have a chat, share our local knowledge and ensure you have everything to make your stay enjoyable, otherwise we pretty much leave you to enjoy your own company.</p>
      <p class="about-text about-sign">- Sam &amp; Julie Harding</p>
      <div class="contact">
        <strong>Contact Us</strong><br>
        Ph: 0400 555 018<br>
        Email: julie@atbellcroft.com.au
      </div>
    </article>

    <article class="panel panel--cabins">
      <h2 class="panel-title">Cabins</h2>
      <div class="cabin-list">
        <div class="cabin cabin--drovers" role="img" aria-label="Photo of a king bed with flowers and a breakfast tray">
          <div class="cabin-label"><h3>Drovers Rest</h3><p>- Luxurious king size bed<br>- Indoor/outdoor spa bath</p></div>
        </div>
        <div class="cabin cabin--wattle" role="img" aria-label="Photo of a timber deck surrounded by garden">
          <div class="cabin-label"><h3>Wattlebird</h3><p>- Hinterland &amp; ocean view<br>Surrounded by<br>fragrant timber<br>campfire furniture</p></div>
        </div>
        <div class="cabin cabin--kirra" role="img" aria-label="Photo of a bright bedroom with white linen">
          <div class="cabin-label"><h3>Kirrabelle</h3><p>- Hinterland &amp; coastal views<br>Spa bath &amp; log fire<br>- King size bed</p></div>
        </div>
        <div class="cabin cabin--lodge" role="img" aria-label="Photo of the lodge verandah looking over the garden">
          <div class="cabin-label"><h3>Lodge</h3><p>- Ocean &amp; hinterland views<br>- 4 bedrooms</p></div>
        </div>
      </div>
    </article>

    <article class="panel panel--rates">
      <h2 class="panel-title">Rates &amp; Packages</h2>
      <div class="rates">
        <div class="rate-head">Couples Cabin,<br>Kirrabelle Guest wing</div>
        <div class="rate-row"><span>7 night Stay</span><span>$1595</span></div>
        <div class="rate-row"><span>Weekend Stay</span><span>$295/Night</span></div>
        <div class="rate-row"><span>Midweek Stay</span><span>$195 - $245/Night</span></div>
        <div class="rate-head">4 Bedroom Lodge</div>
        <div class="rate-row stack"><span>Weekend(2 nights)<br>Up to 8 guests</span><span>$1200</span></div>
        <div class="rate-row stack"><span>Midweek<br>Up to 8 guests</span><span>$275 - $350/Night</span></div>
      </div>
      <div class="inclusions">
        <h4>* Package Inclusions</h4>
        <p>Breakfast hamper, Champagne,<br>Pamper products &amp;<br>complimentary chocolates.</p>
        <h4>* Optional Inclusions</h4>
        <p>Cheese platter<br>&amp;<br>Relaxation massage.</p>
      </div>
    </article>
  </section>

  <!-- Outside sheet -->
  <section class="sheet sheet--outside">
    <article class="panel panel--map">
      <h2 class="map-title">At Bellcroft Map</h2>
      <div class="map" role="img" aria-label="Road map of the hinterland area showing the cottage location">
        <svg width="237" height="528" viewBox="0 0 237 528" aria-hidden="true">
          <path d="M118 130c-9 0-16 7-16 16 0 12 16 28 16 28s16-16 16-28c0-9-7-16-16-16z" fill="#c8102e"/>
          <circle cx="118" cy="146" r="5" fill="#ffffff"/>
        </svg>
      </div>
    </article>

    <article class="panel middle">
      <div class="brand-name">At Bellcroft</div>
      <div class="brand-tag">Bed &amp; breakfast &nbsp; Private cottages</div>
      <div class="address">Bellcroft's Rise<br>24 Ridgeview Road<br>Hillmere QLD 4575<br><br>0400 555 018</div>
    </article>

    <article class="panel front">
      <div class="hero" role="img" aria-label="Photo of a bubbling spa bath on a deck overlooking the hinterland under a blue sky">
        <div class="hero-brand">
          <div class="brand-name">At Bellcroft</div>
          <div class="brand-tag">Bed &amp; breakfast &nbsp; Private cottages</div>
        </div>
      </div>
      <div class="photo photo--hamper" role="img" aria-label="Photo of a breakfast hamper with flowers on white linen"></div>
      <div class="photo photo--view" role="img" aria-label="Photo of champagne glasses on a table with a hinterland view"></div>
      <div class="web-bar">www.atbellcroft.com.au</div>
    </article>
  </section>

</div>
</body>
</html>
```